Redesign My Travel Voucher Coupons-Please redesign the flyers I have attached to this brief.

These designs will be catered towards like travel agency vacation stays...luxury resort stays, hotel and airfare getaways, etc. so must have a travel theme but more importantly professional trustworthy appeal...

Please redesign the flyers I have attached to this brief.

I have attached my existing designs. Please use all existing content and elements exactly but make the design much better...also, please keep in mind that these would be full color and printer friendly...

Target Market(s)

Consumers. People receive these vouchers from businesses that run marketing promotions and contests and giveaways. So the look and feel must feel professional and trustworthy but not cheesy and fake.

Industry/Entity Type

Hotel

Requirements
Must have
• Please use all existing content and elements exactly but make the design much better...also, please keep in mind that these would be full color and printer friendly...

MUST HAVE ALL EXISTING CONTENT EXACT NO EXCEPTIONS
Nice to have
• These designs will be catered towards like travel agency vacation stays...luxury resort stays, hotel and airfare getaways, etc. so must have a travel theme but more importantly professional trustworthy appeal...

Should not have

```html
<!DOCTYPE html>
<html lang="en">
<head>
<meta charset="utf-8">
<title>Hotel Stay Reward Certificate</title>
<link rel="stylesheet" href="https://fonts.googleapis.com/css2?family=Oswald:wght@600;700&family=Open+Sans:wght@400;600;700;800&display=swap">
<style>
  :root {
    --page-bg: #d1d2d4;
    --navy: #141a4d;
    --navy-text: #1b1f5e;
    --ocean: #1f7fc6;
    --sky: #1a9fe0;
    --orange: #f7a33a;
    --orange-deep: #f08c1e;
    --white: #ffffff;
    --link-blue: #1d6fc0;
    --ink: #111111;
    --rule: #777777;
  }
  * { box-sizing: border-box; margin: 0; padding: 0; }
  html, body {
    width: 1200px; height: 1094px; overflow: hidden;
    background: var(--page-bg);
    font-family: "Open Sans", Arial, sans-serif;
  }
  .flyer {
    position: absolute; left: 259px; top: 67px;
    width: 682px; height: 959px; overflow: hidden;
    background: var(--white);
  }
  .flyer-backdrop { position: absolute; inset: 0; }

  .headline { position: absolute; left: 39px; top: 38px; }
  .headline-enjoy {
    font-family: "Oswald", Impact, sans-serif; font-weight: 700;
    font-size: 92px; line-height: 92px; letter-spacing: 1px;
    color: var(--orange);
    -webkit-text-stroke: 3px var(--white); paint-order: stroke fill;
  }
  .headline-pill {
    display: inline-block; margin-top: 4px;
    background: var(--sky); color: var(--white);
    font-weight: 700; font-size: 19px; line-height: 27px;
    padding: 0 14px 0 10px; border-radius: 14px 0 0 14px;
  }
  .headline-detail {
    margin-top: 6px; color: var(--navy-text); font-weight: 800;
    -webkit-text-stroke: 3px var(--white); paint-order: stroke fill;
  }
  .headline-detail .lead { font-size: 16.5px; line-height: 20px; }
  .headline-detail .rest { font-size: 13.5px; line-height: 18px; }

  .sponsor-card {
    position: absolute; left: 442px; top: 0; width: 205px; height: 141px;
    background: var(--white); border-radius: 0 0 14px 14px;
    box-shadow: 0 3px 8px rgba(0,0,0,.35);
    text-align: center; color: var(--navy-text); font-weight: 700;
    padding-top: 24px;
  }
  .sponsor-label { font-size: 11px; }
  .sponsor-brand {
    margin: 14px auto 12px; display: flex; align-items: center; justify-content: center; gap: 6px;
    font-size: 11px; font-weight: 800; color: var(--link-blue); text-transform: uppercase;
  }
  .sponsor-brand .mark { width: 14px; height: 14px; border-radius: 50%; background: var(--link-blue); }
  .sponsor-contact { font-size: 9px; line-height: 12px; }

  .photo-circle {
    position: absolute; width: 150px; height: 150px; border-radius: 50%;
    box-shadow: 0 4px 12px rgba(0,0,0,.45);
  }
  .photo-lobby { left: 118px; top: 274px; background: radial-gradient(circle at 40% 40%, #efe9e4, #b9aaa3 60%, #7f6f6c); }
  .photo-pool { left: 314px; top: 272px; background: linear-gradient(#d9c7c0 0%, #a07263 45%, #4fb0c3 70%, #2e8da3 100%); }
  .photo-suite { left: 501px; top: 242px; background: radial-gradient(circle at 50% 55%, #efe6d8, #a78d6e 60%, #4e3a2c); }

  .section-title {
    font-weight: 700; color: var(--orange-deep);
    font-size: 17px; line-height: 20px; text-transform: uppercase;
  }
  .body-copy { color: var(--white); font-size: 10.4px; line-height: 12.6px; }

  .exclusive { position: absolute; left: 33px; top: 463px; width: 310px; }
  .features { position: absolute; left: 353px; top: 463px; width: 300px; }
  .features .section-title { font-size: 18px; margin-bottom: 4px; }
  .feature-list { list-style: none; }
  .feature-list li {
    display: flex; align-items: center; gap: 6px;
    color: var(--orange); font-weight: 700; font-size: 9.8px; line-height: 12.6px;
  }
  .feature-list svg { width: 10px; height: 10px; flex: none; }

  .how { position: absolute; left: 33px; top: 608px; width: 630px; }
  .testimonial { position: absolute; left: 33px; top: 743px; width: 630px; }
  .testimonial .author { font-weight: 700; }

  .certificate-meta {
    position: absolute; left: 250px; top: 868px; width: 110px;
    text-align: center; color: var(--navy-text);
  }
  .meta-label { font-size: 9px; font-weight: 700; line-height: 11px; }
  .meta-value { font-size: 13px; font-weight: 800; line-height: 15px; color: var(--ink); margin-bottom: 9px; }
  .divider {
    position: absolute; left: 362px; top: 862px; height: 84px;
    border-left: 1px dashed var(--rule);
  }
  .redeem {
    position: absolute; left: 370px; top: 872px; width: 290px; text-align: center;
    color: var(--ink);
  }
  .redeem-lead { font-size: 12px; font-weight: 700; line-height: 15px; }
  .redeem-url { font-size: 16px; font-weight: 800; color: var(--link-blue); line-height: 22px; }
  .redeem-terms { font-size: 7px; line-height: 9px; }
</style>
</head>
<body>
<main class="flyer">
  <svg class="flyer-backdrop" viewBox="0 0 682 959" width="682" height="959">
    <defs>
      <linearGradient id="panelGradient" x1="0" y1="0" x2="1" y2="0.35">
        <stop offset="0" stop-color="#2a8bd3"/>
        <stop offset="0.55" stop-color="#1c3f86"/>
        <stop offset="1" stop-color="#121646"/>
      </linearGradient>
      <linearGradient id="heroGradient" x1="0" y1="0" x2="0" y2="1">
        <stop offset="0" stop-color="#2a3f6a"/>
        <stop offset="0.45" stop-color="#6a6f83"/>
        <stop offset="0.75" stop-color="#b59a7e"/>
        <stop offset="1" stop-color="#4a4b57"/>
      </linearGradient>
      <linearGradient id="waveLight" x1="0" y1="0" x2="1" y2="0">
        <stop offset="0" stop-color="#2f93dc"/>
        <stop offset="1" stop-color="#1a4c93" stop-opacity="0"/>
      </linearGradient>
    </defs>
    <rect width="682" height="959" fill="url(#panelGradient)"/>
    <rect role="img" aria-label="Photo of a resort hotel terrace with lounge seating and parasols at dusk" width="682" height="360" fill="url(#heroGradient)"/>
    <path d="M0,330 C120,350 260,370 420,340 C540,318 620,285 682,275 L682,420 L0,420 Z" fill="url(#panelGradient)"/>
    <path d="M0,345 C110,420 250,460 420,420 C540,392 620,360 682,350 L682,300 C600,320 520,370 400,390 C240,420 110,400 0,345 Z" fill="#1f86d2" opacity="0.85"/>
    <path d="M0,600 C150,560 330,575 500,610 C580,626 640,628 682,622 L682,650 C560,650 420,600 250,600 C140,600 60,620 0,640 Z" fill="url(#waveLight)" opacity="0.7"/>
    <path d="M0,879 C40,905 80,920 130,918 C200,915 250,880 300,856 C370,826 430,818 480,818 C560,820 630,848 682,880 L682,959 L0,959 Z" fill="#ffffff"/>
  </svg>

  <header class="headline">
    <div class="headline-enjoy">ENJOY</div>
    <div class="headline-pill">a 2 Night Hotel Stay</div>
    <div class="headline-detail">
      <div class="lead">of 3+ Star Hotel Accomodations</div>
      <div class="rest">In The City Of Yout Choice Of<br>Over 50 Of The Most Popular<br>Destinations Avaliable!</div>
    </div>
  </header>

  <aside class="sponsor-card">
    <div class="sponsor-label">Compliments Of</div>
    <div class="sponsor-brand"><span class="mark"></span>Brightway Promotions</div>
    <div class="sponsor-contact">Dana Whitfield<br>555-014-2290<br>www.GrowYourClientele.com</div>
  </aside>

  <div class="photo-circle photo-lobby" role="img" aria-label="Photo of guests checking in at a hotel reception desk"></div>
  <div class="photo-circle photo-pool" role="img" aria-label="Photo of a resort pool with palm trees and sun loungers"></div>
  <div class="photo-circle photo-suite" role="img" aria-label="Photo of an elegant hotel bedroom with a tufted headboard"></div>

  <section class="exclusive">
    <h2 class="section-title">Exclusively For :</h2>
    <p class="body-copy">There is no doubt that everyone wishes they can take a much needed vacation to just relax and unwind while having fun at the same time! Enjoy two nights of hotel accommdations in the city of your choice of over 50 of the hottest, most desired vacation spots around the country. Thanks to the business you received this certificate from, now you can enjoy a nice little mini vacation you deserve!</p>
  </section>

  <section class="features">
    <h2 class="section-title">Features :</h2>
    <ul class="feature-list">
      <li><svg viewBox="0 0 10 10"><circle cx="5" cy="5" r="4.2" fill="none" stroke="#f7a33a" stroke-width="1"/><path d="M3,5.2 L4.5,6.6 L7.2,3.6" fill="none" stroke="#f7a33a" stroke-width="1"/></svg>Travel 7 Days A Week</li>
      <li><svg viewBox="0 0 10 10"><circle cx="5" cy="5" r="4.2" fill="none" stroke="#f7a33a" stroke-width="1"/><path d="M3,5.2 L4.5,6.6 L7.2,3.6" fill="none" stroke="#f7a33a" stroke-width="1"/></svg>Good For Two Adults &amp; Two Children</li>
      <li><svg viewBox="0 0 10 10"><circle cx="5" cy="5" r="4.2" fill="none" stroke="#f7a33a" stroke-width="1"/><path d="M3,5.2 L4.5,6.6 L7.2,3.6" fill="none" stroke="#f7a33a" stroke-width="1"/></svg>Multiple Travel Date Requests Allowed</li>
      <li><svg viewBox="0 0 10 10"><circle cx="5" cy="5" r="4.2" fill="none" stroke="#f7a33a" stroke-width="1"/><path d="M3,5.2 L4.5,6.6 L7.2,3.6" fill="none" stroke="#f7a33a" stroke-width="1"/></svg>No Timeshare No Sales Presentation Guaranteed!</li>
      <li><svg viewBox="0 0 10 10"><circle cx="5" cy="5" r="4.2" fill="none" stroke="#f7a33a" stroke-width="1"/><path d="M3,5.2 L4.5,6.6 L7.2,3.6" fill="none" stroke="#f7a33a" stroke-width="1"/></svg>Your Choice Of Over 50 Luxury Destinations</li>
      <li><svg viewBox="0 0 10 10"><circle cx="5" cy="5" r="4.2" fill="none" stroke="#f7a33a" stroke-width="1"/><path d="M3,5.2 L4.5,6.6 L7.2,3.6" fill="none" stroke="#f7a33a" stroke-width="1"/></svg>Pay Just The Taxes &amp; Fees</li>
      <li><svg viewBox="0 0 10 10"><circle cx="5" cy="5" r="4.2" fill="none" stroke="#f7a33a" stroke-width="1"/><path d="M3,5.2 L4.5,6.6 L7.2,3.6" fill="none" stroke="#f7a33a" stroke-width="1"/></svg>Fully Transferable To Another Person</li>
      <li><svg viewBox="0 0 10 10"><circle cx="5" cy="5" r="4.2" fill="none" stroke="#f7a33a" stroke-width="1"/><path d="M3,5.2 L4.5,6.6 L7.2,3.6" fill="none" stroke="#f7a33a" stroke-width="1"/></svg>24 Months To Complete Travel After Redemption</li>
    </ul>
  </section>

  <section class="how">
    <h2 class="section-title">How We Can Do This?</h2>
    <p class="body-copy">We contract with the world leading hotel chains and resorts to help them fill their otherwise empty rooms.<br>
    We help fill empty rooms which the hotels, resorts and cruise lines turn into additional revenue from other areas of their property and futur bookings.<br>
    Hotels rarely experience full occupancy, yet they remain open, providing rooms and services at fixed costs. So when hotels give out their rooms by partnering with marketing companies like us, they might miss out on the room fee, but they already didn't have that in the first place, at least now they have the opportunity to gain a customer for their in-house restaurants, room service, their casinos, an extra day stay, future bookings, etc.</p>
  </section>

  <section class="testimonial">
    <h2 class="section-title">What Other Say</h2>
    <p class="body-copy">"Being able to stay right on the strip in Las Vegas was great. I love that we were able to walk around to all the sites and attractions. The fountains at the Bellmare were AMAZING! The Gondola ride at the Lagoon Palace was very nice. I LOVED the atmo-sphere and the food. The whole experience was awesome. THANK YOU!"<br>
    <span class="author">Marissa K. San Diego, CA</span></p>
  </section>

  <div class="certificate-meta">
    <div class="meta-label">Certificate ID</div>
    <div class="meta-value">107083-11266</div>
    <div class="meta-label">Expires</div>
    <div class="meta-value">11/07/2020</div>
  </div>
  <div class="divider"></div>
  <div class="redeem">
    <div class="redeem-lead">VIEW ALL THE DETAILS OF THIS SPECIAL OFFER<br>AND REDEEM ONLINE AT</div>
    <div class="redeem-url">WWW.STAYANDSAVEREWARDS.COM</div>
    <div class="redeem-terms">*Terms and Conditions apply see website for details</div>
  </div>
</main>
</body>
</html>
```